Woo Commerce Redesign

We have a website--www.lessonharborbooks.com (a woocommerce theme on Word Press) and are looking for someone to customize the design for us so it is better optimized, more intuitive and has a nicer look and feel.

The only design element we need to keep is the logo.

Our primary aim is to get the value proposition at the top of the page. I am thinking this means that we need to design the header but we will accept better options as well.

Our three-fold value prop is:
Price Match Guarantee
*Free Shipping
Same Day Service

*free shipping is on orders over $45

Internal Category Pages:
We also need to design an internal landing page template optimized for both computer and mobile users so that when an individual clicks on an ad, they come to a page that answers those important questions of who are they? Why should I buy from them? and what do they offer?

We expect this copy to be something like the following:
“Welcome to Lesson Harbor, your one stop place for [math curriculum] for both schools and homeschoolers.
Our price match guarantee, free shipping and same day service make us the perfect partner for all of your curriculum needs!
Click here to see all of our [math] titles for grades 1-12 or select the grade you are looking for and you will find all of the available [math] products.

Reason: I am extending this deadline because I did not get feedback to the designers over the weekend. I will provide feedback in the next few days so we can get a final design.

```html
<!DOCTYPE html>
<html lang="en">
<head>
<meta charset="utf-8">
<title>Lesson Harbor – Home</title>
<link rel="stylesheet" href="https://fonts.googleapis.com/css2?family=Open+Sans:wght@300;400;600;700&display=swap">
<style>
:root{
  --orange:#f0731f;
  --ink:#1c1c1c;
  --blue:#1f5fbf;
  --text:#444;
  --panel:#f4f4f4;
  --line:#dddddd;
  --white:#fff;
  --footer:#1e1e1e;
}
*{box-sizing:border-box;margin:0;padding:0}
html,body{width:755px;height:1200px;overflow:hidden;font-family:'Open Sans',sans-serif;color:var(--text);background:var(--white)}
.wrap{width:631px;margin-left:62px;position:relative}
.topbar{height:22px;background:var(--orange);color:var(--white);font-size:7.5px}
.topbar .wrap{display:flex;justify-content:space-between;align-items:center;height:22px}
.topbar .links span{margin-left:6px;padding-left:6px;border-left:1px solid rgba(255,255,255,.5)}
.topbar .links span:first-child{border:0}
.masthead{height:80px;background:var(--ink)}
.masthead .wrap{display:flex;align-items:center;height:80px}
.brand{display:flex;align-items:center;gap:8px;color:var(--white);font-size:30px;font-weight:600;letter-spacing:-.5px;width:283px}
.brand i{width:14px;height:14px;background:var(--orange);display:block}
.search{width:221px;height:23px;border:1px solid #3a3a3a;color:#999;font-size:7.5px;display:flex;align-items:center;justify-content:space-between;padding:0 10px}
.cart{margin-left:15px;width:112px;height:23px;border:1px solid #3a3a3a;color:#ccc;font-size:7.5px;display:flex;align-items:center;gap:7px;padding:0 9px}
.nav{height:30px;background:var(--blue)}
.nav .wrap{display:flex;height:30px;align-items:center;color:var(--white);font-size:8.8px}
.nav .item{height:30px;display:flex;align-items:center;padding:0 13px;border-right:1px solid rgba(255,255,255,.15)}
.nav .item.home{background:var(--orange)}
.nav .connect{margin-left:auto;display:flex;gap:6px;align-items:center}
.nav .connect i{width:7px;height:7px;background:var(--white);border-radius:50%;display:block}
.hero{height:330px;position:relative;background:linear-gradient(180deg,#8a7a62 0%,#b08a55 35%,#6e5538 70%,#3a2a1c 100%)}
.hero svg{position:absolute;left:0;top:0}
.hero h2{position:absolute;top:138px;width:755px;text-align:center;color:var(--white);font-size:19px;font-weight:700}
.hero .props{position:absolute;top:180px;left:120px;width:520px;display:flex;justify-content:space-between;color:var(--white);font-size:12.5px;font-weight:300}
.welcome{height:168px;text-align:center;padding-top:30px}
.welcome h1{font-size:23px;font-weight:400;color:#333;margin-bottom:12px}
.welcome p{font-size:7.6px;line-height:14.5px;width:631px;margin:0 auto 11px}
.featured{height:356px;background:var(--panel)}
.featured h3{padding-top:26px;font-size:15.5px;font-weight:600;color:#333;height:58px;border-bottom:1px solid var(--line)}
.featured .pager{position:absolute;right:0;top:30px;display:flex;gap:4px}
.featured .pager span{width:15px;height:14px;border:1px solid #bbb;font-size:8px;text-align:center;line-height:12px;color:#777}
.cards{display:flex;gap:19px;margin-top:34px}
.card{width:144px;height:218px;background:var(--white);border:1px solid var(--line);text-align:center;padding-top:15px;position:relative}
.card .cover{width:80px;height:80px;margin:0 auto 18px;background:linear-gradient(135deg,#7a4a30,#c9a26a 50%,#3d5a8a)}
.card .title{font-size:8.6px;line-height:12px;color:#444;padding:0 12px}
.card .price{font-size:8.8px;font-weight:600;margin-top:4px}
.card .price s{color:#333;margin-right:20px}
.card .price b{color:var(--orange);font-weight:600}
.card .btn{position:absolute;left:27px;bottom:20px;width:88px;height:24px;background:var(--orange);color:var(--white);font-size:9.5px;line-height:24px}
.footer{height:214px;background:var(--footer);color:#ccc}
.footer .cols{display:flex;padding-top:28px;height:170px}
.footer h4{font-size:10.5px;font-weight:400;color:var(--white);margin-bottom:12px}
.footer ul{list-style:none;font-size:8.6px;line-height:20px}
.col1{width:239px;display:flex;gap:60px;border-right:1px solid #2c2c2c}
.col2{width:186px;border-right:1px solid #2c2c2c}
.contact{font-size:8.6px;line-height:20px}
.col3{padding-left:22px;width:206px}
.col3 p{font-size:8px;color:#888;margin-bottom:6px}
.sub{display:flex;height:24px;margin-left:2px}
.sub span{width:138px;background:var(--white);color:#aaa;font-size:6.5px;line-height:24px;padding-left:10px}
.sub b{width:66px;background:var(--orange);color:var(--white);font-size:8.5px;text-align:center;line-height:24px}
.socials{display:flex;gap:8px;margin:10px 0 0 2px}
.socials i{width:24px;height:24px;border-radius:50%;background:var(--white);display:block}
.bottom{border-top:1px solid #555;height:44px;display:flex;justify-content:space-between;align-items:center;font-size:7.5px;color:#999}
.pay{display:flex;align-items:center;gap:8px}
.pay i{width:21px;height:13px;display:block;background:#ddd}
.pay i.b{background:#1f4f9f}
</style>
</head>
<body>
<header>
  <div class="topbar"><div class="wrap">
    <div>☎ Call Us : 800-555-0142 &nbsp;&nbsp;|&nbsp;&nbsp; Fax : 610-555-0198</div>
    <div class="links"><span>Contact Us</span><span>Resources</span><span>About</span><span>Newsletter</span><span>My Account</span><span>Cart</span></div>
  </div></div>
  <div class="masthead"><div class="wrap">
    <div class="brand"><i></i>Lesson Harbor</div>
    <div class="search">Search entire store here...
      <svg width="8" height="8" viewBox="0 0 10 10"><circle cx="4" cy="4" r="3" fill="none" stroke="#999" stroke-width="1.4"/><line x1="6.3" y1="6.3" x2="9" y2="9" stroke="#999" stroke-width="1.4"/></svg></div>
    <div class="cart"><svg width="12" height="10" viewBox="0 0 12 10"><path d="M0 1h2l2 6h6l1.5-4.5H3" fill="none" stroke="#f0731f" stroke-width="1.4"/><circle cx="5" cy="9" r="1" fill="#f0731f"/><circle cx="9" cy="9" r="1" fill="#f0731f"/></svg>CART (EMPTY)<span style="margin-left:auto">⌄</span></div>
  </div></div>
  <nav class="nav"><div class="wrap">
    <div class="item home">HOME</div>
    <div class="item">FILTER BY GRADE ⌄</div>
    <div class="item">FILTER BY SUBJECT ⌄</div>
    <div class="item">FILTER BY PUBLISHER ⌄</div>
    <div class="item">ONLINE COURSES</div>
    <div class="connect">CONNECT US : <i></i><i></i><i></i><i></i></div>
  </div></nav>
</header>

<section class="hero" role="img" aria-label="Photo of an open-air riverside book market with rows of used books at sunset">
  <svg width="755" height="330" viewBox="0 0 755 330">
    <polygon points="108,122 692,122 652,222 62,222" fill="#f0731f" opacity=".93"/>
    <polyline points="30,176 24,186 30,196" fill="none" stroke="#fff" stroke-width="1"/>
    <polyline points="722,176 728,186 722,196" fill="none" stroke="#fff" stroke-width="1"/>
  </svg>
  <h2>FREE SHIPPING IS ON ORDERS OVER $45</h2>
  <div class="props"><span>✔ Price Match Guarantee</span><span>✔ Free Shipping</span><span>✔ Same Day Service</span></div>
</section>

<section class="welcome">
  <h1>Welcome to Lesson Harbor</h1>
  <p>Welcome to Lesson Harbor, your one stop place for [math curriculum] for both schools and homeschoolers. Our price match guarantee, free shipping and same day service make us the perfect partner for all of your curriculum needs!</p>
  <p>Click here to see all of our [math] titles for grades 1-12 or select the grade you are looking for and you will find all of the available [math] products.</p>
</section>

<section class="featured"><div class="wrap">
  <h3>FEATURED PRODUCTS</h3>
  <div class="pager"><span>‹</span><span>›</span></div>
  <div class="cards">
    <div class="card"><div class="cover" role="img" aria-label="Audio album cover"></div><div class="title">Brave Voyages Volume 1 by Tale Time Hour®</div><div class="price"><s>$22.50</s><b>$18.00</b></div><div class="btn">ADD TO CART</div></div>
    <div class="card"><div class="cover" role="img" aria-label="Audio album cover"></div><div class="title">Bold Moments Volume 1 by Tale Time Hour®</div><div class="price"><s>$14.00</s><b>$11.20</b></div><div class="btn">ADD TO CART</div></div>
    <div class="card"><div class="cover" role="img" aria-label="Audio album cover"></div><div class="title">Roots of Our Nation presented by Tale Time Hour®</div><div class="price"><s>$45.00</s><b>$36.00</b></div><div class="btn">ADD TO CART</div></div>
    <div class="card"><div class="cover" role="img" aria-label="Audio album cover"></div><div class="title">Paths of Courage Series presented by Tale Time Hour®</div><div class="price"><s>$45.00</s><b>$36.00</b></div><div class="btn">ADD TO CART</div></div>
  </div>
</div></section>

<footer class="footer"><div class="wrap">
  <div class="cols">
    <div class="col1">
      <div><h4>USEFULL LINKS</h4><ul><li>Products</li><li>My Account</li><li>My Cart</li><li>Privacy Policy</li><li>Terms and Conditions</li></ul></div>
      <div style="padding-top:25px"><ul><li>Specials</li><li>Portfolio</li><li>FAQ</li><li>Contact</li><li>Others</li></ul></div>
    </div>
    <div class="col2">
      <h4>CONTACT INFO</h4>
      <div class="contact">
        <div>Lesson Harbor, 58 Quayside Lane,</div>
        <div>Millbrook PA 18900</div>
        <div>☎ 800-555-0142</div>
        <div>✉ hello@lessonharbor.example</div>
      </div>
    </div>
    <div class="col3">
      <h4>SIGN UP FOR NEWSLETTERS</h4>
      <p>Please sign up here for latest news</p>
      <div class="sub"><span>EMAIL ADDRESS</span><b>SUBSCRIBE</b></div>
      <div class="socials"><i></i><i></i><i></i><i></i></div>
    </div>
  </div>
  <div class="bottom">
    <div>© 2017 Lesson Harbor Ltd. &nbsp;All right reserved. &nbsp;Term of Use</div>
    <div class="pay">Payments: <i></i><i></i><i class="b"></i><i></i></div>
  </div>
</div></footer>
</body>
</html>
```